Re-design of Business Card

We require a design for our business card.

Korrim is a supplier of industrial packaging specializing in plastic products. We are undergoing a rebranding to appear more corporate. We have changed our company name to korrim and have a new logo.

I have uploaded our old card design with the previous company name.
Don't copy the current design. We are looking for a new design.

Industry/Entity Type

Manufacturing

Contact Information for Business Card

please don't copy the current design. we are looking for a new design.

Font styles to use
Sans Serif

Colors

Designer to choose colors to be used in the design.

Requirements
Must have
• clean and easy to read.

```html
<!DOCTYPE html>
<html lang="en">
<head>
<meta charset="utf-8">
<title>Korrim Business Card</title>
<link href="https://fonts.googleapis.com/css2?family=Lato:wght@400;700;900&display=swap" rel="stylesheet">
<style>
  :root {
    --backdrop: #3a322d;
    --card: #0b0b0c;
    --mark-grey: #6a6a6c;
    --accent: #f08a1c;
    --text: #f2f2f2;
  }
  * { margin: 0; padding: 0; box-sizing: border-box; }
  html, body {
    width: 1200px; height: 847px; overflow: hidden;
    background: var(--backdrop);
    font-family: "Lato", sans-serif;
  }
  .sheet {
    position: relative; width: 1200px; height: 847px;
    display: flex; align-items: center; justify-content: center; gap: 40px;
  }
  .card {
    position: relative; width: 540px; height: 310px;
    background: var(--card);
    box-shadow: 0 10px 30px rgba(0,0,0,0.45);
  }
  .card-front { display: flex; align-items: center; justify-content: center; }
  .brand-name {
    font-weight: 900; font-size: 76px; letter-spacing: 2px;
    color: var(--mark-grey); text-transform: uppercase;
  }
  .card-back { color: var(--text); }
  .identity {
    position: absolute; left: 60px; top: 100px; text-align: right; width: 170px;
  }
  .person-name { color: var(--accent); font-weight: 700; font-size: 27px; line-height: 1.1; white-space: nowrap; }
  .person-role { font-size: 14px; margin-top: 4px; white-space: nowrap; }
  .divider {
    position: absolute; left: 248px; top: 92px; width: 2px; height: 80px;
    background: var(--accent);
  }
  .contact { position: absolute; left: 268px; top: 100px; font-size: 14px; line-height: 1.45; }
  .contact-row { display: flex; align-items: center; gap: 8px; }
  .contact-row svg { width: 13px; height: 13px; fill: var(--accent); flex: none; }
  .address { margin-bottom: 4px; }
  .website {
    position: absolute; left: 0; right: 0; bottom: 44px; text-align: center;
    font-size: 15px; letter-spacing: 6px;
  }
</style>
</head>
<body>
<main class="sheet">
  <section class="card card-front">
    <div class="brand-name">Korrim</div>
  </section>

  <section class="card card-back">
    <div class="identity">
      <div class="person-name">Darren Holt</div>
      <div class="person-role">Machinery Sales Manager</div>
    </div>
    <div class="divider"></div>
    <div class="contact">
      <div class="address">48 Marlow St Eastbrook Heights,<br>Qld 4102 Australia</div>
      <div class="contact-row">
        <svg viewBox="0 0 24 24" aria-hidden="true"><path d="M6.6 10.8a15.1 15.1 0 0 0 6.6 6.6l2.2-2.2c.3-.3.7-.4 1-.2 1.1.4 2.3.6 3.6.6.6 0 1 .4 1 1V20c0 .6-.4 1-1 1A17 17 0 0 1 3 4c0-.6.4-1 1-1h3.5c.6 0 1 .4 1 1 0 1.3.2 2.5.6 3.6.1.3 0 .7-.2 1z"/></svg>
        <span>1300 555 018</span>
      </div>
      <div class="contact-row">
        <svg viewBox="0 0 24 24" aria-hidden="true"><path d="M2 5h20v14H2zm2 2v.5l8 5 8-5V7zm0 2.8V17h16V9.8l-8 5z"/></svg>
        <span>darren@korrim.com.au</span>
      </div>
    </div>
    <div class="website">www.korrim.com.au</div>
  </section>
</main>
</body>
</html>
```